Business that Cleans the dishes and utensils used in private jets needs a flyer to describe its b...

I need a flyer to describe a HK based company called 'Velmora Services'. We help the flight attendants to clean valuable dishes and utensils to save them time and costs. Color green is preferable. The design shall be easy to read and clear

Target Market(s)

Flight attendants and flight operations management

Industry/Entity Type

Aviation

Colors

Designer to choose colors to be used in the design.

Requirements
Must have
• Clean and professional.

```html
<!DOCTYPE html>
<html lang="en">
<head>
<meta charset="utf-8">
<title>Velmora Services – Flyer</title>
<link href="https://fonts.googleapis.com/css2?family=Montserrat:wght@700;800&family=Roboto+Condensed:wght@400;700&display=swap" rel="stylesheet">
<style>
  :root {
    --green-light: #8cc63f;
    --green-mid: #63b246;
    --green-deep: #215229;
    --green-dark: #1c4a24;
    --green-hill: #4f8a3a;
    --yellow: #ffe600;
    --white: #ffffff;
    --ink: #111111;
  }
  html, body { margin: 0; padding: 0; overflow: hidden; }
  body { width: 927px; height: 1200px; background: var(--green-light); }
  .flyer {
    position: relative; width: 927px; height: 1200px; overflow: hidden;
    background: linear-gradient(180deg, var(--green-mid) 0%, var(--green-light) 60%);
    font-family: "Roboto Condensed", Arial, sans-serif;
  }
  .backdrop { position: absolute; inset: 0; }
  .airport-scene {
    position: absolute; left: 0; top: 360px; width: 927px; height: 340px;
    background: linear-gradient(180deg, rgba(140,198,63,0) 0%, rgba(120,185,60,0.55) 55%, rgba(140,198,63,0.2) 100%);
  }
  .brand {
    position: absolute; left: 112px; top: 120px; width: 440px;
    font-family: "Montserrat", Arial, sans-serif; font-weight: 800;
    font-size: 50px; line-height: 1.05; color: var(--yellow); margin: 0;
  }
  .plates-art {
    position: absolute; left: 552px; top: 104px; width: 320px; height: 240px;
    border-radius: 120px;
    background: radial-gradient(ellipse at 60% 50%, #eef6fb 0%, #d9e7ee 55%, rgba(200,210,215,0.6) 100%);
  }
  .headline {
    position: absolute; left: 0; width: 927px; top: 452px; margin: 0; text-align: center;
    font-family: "Montserrat", Arial, sans-serif; font-weight: 800;
    font-size: 43px; line-height: 56px; color: var(--white); letter-spacing: -0.5px;
  }
  .tagline {
    position: absolute; left: 0; width: 927px; top: 578px; margin: 0; text-align: center;
    font-size: 28px; line-height: 37px; color: var(--ink);
  }
  .services-icon {
    position: absolute; left: 422px; top: 698px; width: 114px; height: 86px;
    border-radius: 43px;
    background: radial-gradient(ellipse at 50% 50%, #e6f1f7 0%, #cfdde4 70%, rgba(200,210,215,0.5) 100%);
  }
  .services-title {
    position: absolute; left: 0; width: 927px; top: 814px; margin: 0; text-align: center;
    font-size: 27px; font-weight: 400; color: var(--white);
  }
  .service-list {
    position: absolute; top: 874px; margin: 0; padding: 0; list-style: none;
    color: var(--white); font-size: 18px; line-height: 23.6px;
  }
  .service-list.left { left: 58px; width: 410px; }
  .service-list.right { left: 487px; width: 420px; }
  .service-list li { position: relative; padding-left: 30px; }
  .service-list li svg { position: absolute; left: 0; top: 3px; width: 20px; height: 18px; }
  .service-list li.small { font-size: 15px; line-height: 20px; margin-top: 14px; }
  .contact-bar {
    position: absolute; left: 0; top: 1066px; width: 927px; height: 88px;
    background: var(--yellow); display: flex; align-items: center; justify-content: center;
    font-size: 43px; color: var(--green-deep); gap: 14px;
  }
  .contact-bar .phone { font-weight: 700; }
  .footer-band { position: absolute; left: 0; top: 1154px; width: 927px; height: 46px; background: var(--green-deep); }
</style>
</head>
<body>
<main class="flyer">
  <svg class="backdrop" width="927" height="1200" viewBox="0 0 927 1200" aria-hidden="true">
    <defs>
      <linearGradient id="heroDark" x1="0" y1="0" x2="0" y2="1">
        <stop offset="0" stop-color="#3a8a35"/>
        <stop offset="1" stop-color="#1f5128"/>
      </linearGradient>
    </defs>
    <path d="M0 0 H825 C790 190 650 410 410 418 C240 424 100 360 0 290 Z" fill="#e2efd7"/>
    <path d="M0 0 H808 C770 180 640 395 410 404 C240 410 100 345 0 272 Z" fill="url(#heroDark)"/>
    <path d="M0 800 C250 700 600 670 927 720 V1200 H0 Z" fill="var(--green-hill)"/>
    <path d="M0 810 C260 720 600 700 927 760 V1200 H0 Z" fill="var(--green-deep)"/>
  </svg>

  <div class="airport-scene" role="img" aria-label="Illustrated airport terminal with a parked jet, control tower and waiting seats"></div>

  <h1 class="brand">Velmora Services</h1>
  <div class="plates-art" role="img" aria-label="Illustration of two clean dinner plates with sparkles"></div>

  <h2 class="headline">THE BEST WAY TO<br>CLEAN DISHES</h2>
  <p class="tagline">We help the flight attendants to clean<br>valuable dishes and utensils to save them time and costs</p>

  <div class="services-icon" role="img" aria-label="Small illustration of two stacked plates"></div>
  <h3 class="services-title">Our Services</h3>

  <ul class="service-list left">
    <li><svg viewBox="0 0 20 18"><path d="M2 10 L8 15 L18 2" fill="none" stroke="var(--yellow)" stroke-width="3.5" stroke-linecap="round"/></svg>General household cleaning; deep cleanings, regular maintenance cleanings, etc.</li>
    <li><svg viewBox="0 0 20 18"><path d="M2 10 L8 15 L18 2" fill="none" stroke="var(--yellow)" stroke-width="3.5" stroke-linecap="round"/></svg>Move ins and move outs.</li>
    <li><svg viewBox="0 0 20 18"><path d="M2 10 L8 15 L18 2" fill="none" stroke="var(--yellow)" stroke-width="3.5" stroke-linecap="round"/></svg>Laundry: Wash, fold and put away.</li>
    <li><svg viewBox="0 0 20 18"><path d="M2 10 L8 15 L18 2" fill="none" stroke="var(--yellow)" stroke-width="3.5" stroke-linecap="round"/></svg>Blinds: Carefully dusted or damp wiped.</li>
    <li><svg viewBox="0 0 20 18"><path d="M2 10 L8 15 L18 2" fill="none" stroke="var(--yellow)" stroke-width="3.5" stroke-linecap="round"/></svg>Organizing.</li>
    <li><svg viewBox="0 0 20 18"><path d="M2 10 L8 15 L18 2" fill="none" stroke="var(--yellow)" stroke-width="3.5" stroke-linecap="round"/></svg>Unpacking boxes and putting contents away.</li>
  </ul>

  <ul class="service-list right">
    <li><svg viewBox="0 0 20 18"><path d="M2 10 L8 15 L18 2" fill="none" stroke="var(--yellow)" stroke-width="3.5" stroke-linecap="round"/></svg>Floors hand washed or mopped.</li>
    <li><svg viewBox="0 0 20 18"><path d="M2 10 L8 15 L18 2" fill="none" stroke="var(--yellow)" stroke-width="3.5" stroke-linecap="round"/></svg>Windows washed upon request.</li>
    <li><svg viewBox="0 0 20 18"><path d="M2 10 L8 15 L18 2" fill="none" stroke="var(--yellow)" stroke-width="3.5" stroke-linecap="round"/></svg>Inside of appliances cleaned upon request.</li>
    <li><svg viewBox="0 0 20 18"><path d="M2 10 L8 15 L18 2" fill="none" stroke="var(--yellow)" stroke-width="3.5" stroke-linecap="round"/></svg>Detailed kitchen cleanings including washing</li>
    <li class="small"><svg viewBox="0 0 20 18"><path d="M2 10 L8 15 L18 2" fill="none" stroke="var(--yellow)" stroke-width="3.5" stroke-linecap="round"/></svg>Ala carte service: You leave us your list and it<br>can change from visit to visit.<br>Party set-up and clean-up.</li>
  </ul>

  <div class="contact-bar">
    <span class="phone">852 3018 4726</span>
    <span class="divider">|</span>
    <span class="web">www.velmoraservices.com</span>
  </div>
  <div class="footer-band"></div>
</main>
</body>
</html>
```